logo for new brand name "Veltro"
The real quality
Project: logo for new brand name "Veltro"
logo for new brand name "Veltro" - Construction
Creative Brief
Modern
Samer Bouhadi
Marketing Manager
Harbor District, Qadira - info@nawrasmekan.com.sa www.nawrasmekan.com.sa
samer@bouhadi.net
www.nawrasmekan.com.sa

```html
<!DOCTYPE html>
<html lang="en">
<head>
<meta charset="utf-8">
<title>Veltro Stationery</title>
<link href="https://fonts.googleapis.com/css2?family=Open+Sans:wght@400;600;700&display=swap" rel="stylesheet">
<style>
:root{
  --bg:#e9e4dc;
  --paper:#ffffff;
  --red:#e8242c;
  --red-faint:#fbe9e8;
  --ink:#333333;
  --muted:#8a8a8a;
  --line:#cfcfcf;
  --black:#111111;
}
*{box-sizing:border-box;margin:0;padding:0}
html,body{width:1200px;height:679px;overflow:hidden}
body{background:var(--bg);font-family:"Open Sans",sans-serif;color:var(--ink);position:relative}
.piece{position:absolute;background:var(--paper);box-shadow:0 2px 6px rgba(0,0,0,.25);overflow:hidden}
.label{position:absolute;z-index:5;font-size:7px;font-weight:600;color:#3a3a3a;text-align:center;white-space:nowrap}
.brand{display:flex;flex-direction:column;align-items:center;color:var(--red);font-weight:600}
.brand .dot{border-radius:50%;background:var(--red)}
.brand .name{line-height:1;letter-spacing:.5px}
.tab{position:absolute;left:0;width:6px;background:var(--red)}
.faint-mark{position:absolute;border-radius:50%;background:var(--red-faint)}
.footer{position:absolute;left:0;right:0;text-align:center;font-size:4px;color:var(--muted);line-height:1.5}

/* fax */
.fax{left:19px;top:96px;width:258px;height:546px}
.fax .brand{position:absolute;top:14px;left:0;right:0}
.fax .fax-title{position:absolute;right:14px;top:48px;font-size:7px;font-weight:700}
.fax-table{position:absolute;left:14px;top:56px;border-collapse:collapse;font-size:5px;width:230px}
.fax-table td{border:1px solid var(--line);height:13px;padding:0 3px}
.fax-table td.k{width:26px}
.checks{position:absolute;left:14px;right:14px;top:122px;display:flex;justify-content:space-between;font-size:4.5px}
.checks span::before{content:"";display:inline-block;width:5px;height:5px;border:1px solid #999;margin-right:3px;vertical-align:middle}

/* letterhead */
.letter{left:298px;top:96px;width:316px;height:552px}
.letter .brand{position:absolute;top:14px;left:0;right:0}

/* envelopes */
.env-front{left:631px;top:168px;width:550px;height:252px}
.env-front .brand{position:absolute;left:16px;top:18px;align-items:flex-start}
.env-front .addr{position:absolute;left:16px;top:62px;font-size:4.5px;color:var(--muted);line-height:1.5}
.env-back1{left:631px;top:439px;width:550px;height:118px}
.env-back2{left:792px;top:475px;width:389px;height:154px}
.env-back2 .brand{position:absolute;left:0;right:0;top:14px;color:#fff}
.env-back2 .brand .dot{background:#fff}

/* cards */
.card{top:36px;width:132px;height:60px;border-radius:3px}
.card-front{left:511px}
.card-front .tab{width:4px;top:0;height:60px}
.card-front .who{position:absolute;right:10px;top:8px;text-align:right;font-size:4.5px;line-height:1.5}
.card-front .who b{color:var(--red);font-size:5px}
.card-front .contact{position:absolute;right:10px;bottom:7px;text-align:right;font-size:3.6px;color:var(--muted);line-height:1.5}
.card .brand{position:absolute;left:0;right:0;top:16px}
.card-b1{left:677px}
.card-b2{left:845px;background:var(--black)}
.card-b3{left:1013px;background:var(--red)}
.card-b3 .brand{color:#fff}.card-b3 .brand .dot{background:#fff}
</style>
</head>
<body>

<div class="label" style="left:19px;top:84px;width:258px">Fax Cover</div>
<div class="label" style="left:298px;top:84px;width:316px">Letterhead</div>
<div class="label" style="left:631px;top:156px;width:550px;text-align:left">Envelope (Front)</div>
<div class="label" style="left:631px;top:428px;width:550px">Envelope (Back) Option 1</div>
<div class="label" style="left:792px;top:464px;width:389px">Envelope (Back) Option 2</div>
<div class="label" style="left:511px;top:26px;width:132px">Business Card (Front)</div>
<div class="label" style="left:677px;top:26px;width:132px">Business Card (Back) Option 1</div>
<div class="label" style="left:845px;top:26px;width:132px">Business Card (Back) Option 2</div>
<div class="label" style="left:1013px;top:26px;width:132px">Business Card (Back) Option 3</div>

<section class="piece fax">
  <div class="tab" style="top:12px;height:26px"></div>
  <div class="faint-mark" style="left:22px;top:250px;width:200px;height:200px"></div>
  <div class="brand"><span class="dot" style="width:14px;height:14px"></span><span class="name" style="font-size:10px">veltro</span></div>
  <div class="fax-title">FAX</div>
  <table class="fax-table">
    <tr><td class="k">To:</td><td></td><td class="k">From:</td><td></td></tr>
    <tr><td class="k">Fax:</td><td></td><td class="k">Pages:</td><td></td></tr>
    <tr><td class="k">Phone:</td><td></td><td class="k">Date:</td><td></td></tr>
    <tr><td class="k">Re:</td><td></td><td class="k">CC:</td><td></td></tr>
  </table>
  <div class="checks"><span>Urgent</span><span>For Review</span><span>Please Comment</span><span>Please Reply</span><span>Please Recycle</span></div>
  <div class="footer" style="bottom:10px">Harbor District, Qadira &nbsp;|&nbsp; +000 11 555 0142<br>hello@veltro.example &nbsp;|&nbsp; www.veltro.example</div>
</section>

<section class="piece letter">
  <div class="tab" style="top:12px;height:26px"></div>
  <div class="faint-mark" style="left:58px;top:200px;width:200px;height:200px"></div>
  <div class="brand"><span class="dot" style="width:14px;height:14px"></span><span class="name" style="font-size:10px">veltro</span></div>
  <div class="footer" style="bottom:10px">Harbor District, Qadira &nbsp;|&nbsp; +000 11 555 0142<br>hello@veltro.example &nbsp;|&nbsp; www.veltro.example</div>
</section>

<section class="piece env-front">
  <div class="tab" style="top:0;height:22px"></div>
  <div class="brand"><span class="dot" style="width:22px;height:22px"></span><span class="name" style="font-size:10px">veltro</span></div>
  <div class="addr">Harbor District, Qadira<br>www.veltro.example</div>
</section>

<section class="piece env-back1">
  <svg width="550" height="118" viewBox="0 0 550 118" aria-hidden="true">
    <polyline points="0,0 275,62 550,0" fill="none" stroke="#d6d6d6" stroke-width="1"/>
    <polyline points="0,118 200,56" fill="none" stroke="#e2e2e2"/>
    <polyline points="550,118 350,56" fill="none" stroke="#e2e2e2"/>
  </svg>
</section>

<section class="piece env-back2">
  <svg width="389" height="154" viewBox="0 0 389 154" style="position:absolute;left:0;top:0" aria-hidden="true">
    <polygon points="0,0 389,0 389,20 194,78 0,20" fill="#e8242c"/>
    <polyline points="0,154 150,84" fill="none" stroke="#e2e2e2"/>
    <polyline points="389,154 240,84" fill="none" stroke="#e2e2e2"/>
  </svg>
  <div class="brand"><span class="dot" style="width:12px;height:12px"></span><span class="name" style="font-size:8px">veltro</span></div>
</section>

<section class="piece card card-front">
  <div class="tab"></div>
  <div class="who"><b>Samer Bouhadi</b><br>Marketing Manager</div>
  <div class="contact">+000 11 555 0142<br>samer@veltro.example<br>www.veltro.example<br>Harbor District, Qadira</div>
</section>
<section class="piece card card-b1">
  <div class="brand"><span class="dot" style="width:12px;height:12px"></span><span class="name" style="font-size:8px">veltro</span></div>
</section>
<section class="piece card card-b2">
  <div class="brand"><span class="dot" style="width:12px;height:12px"></span><span class="name" style="font-size:8px">veltro</span></div>
</section>
<section class="piece card card-b3">
  <div class="brand"><span class="dot" style="width:12px;height:12px"></span><span class="name" style="font-size:8px">veltro</span></div>
</section>

</body>
</html>
```